wooden jewelry - pearl necklaces

I sell wooden jeweler (rings and pearls) on markets, and so on. I also opened my business as a carpenter. The rings and a combination of wood and metal. The wood is special wood, not very common on Europe. I paint the rings afterwards. You can see some of the pictures on the pictures I uploaded. The pearls are made of the same kind of wood and colored in all kinds of colors. They are then assembled to bracelets. The jewelry is very individual and looks really cool and all kinds of people.

Target Market(s)

Young urban alternative with a sense of individuality

Contact Information for Business Card

Front:

Text:

„Kugelwerk“ (big)
„Malte Oswitz“ (smaler)

Back
„Holzschmuck
Herstellung von individuellem Holz- und Modeschmuck

Malte Oswitz
Tel: 015239460518
Lindgarbweg 9
83127 Holmbach

malteoswitz@postfeld.de“

Font styles to use
Sans Serif

Requirements
Nice to have
• Nice to see a camel thorn tree on the background, this is a special wood and some of the rings are made out of this wood.

```html
<!DOCTYPE html>
<html lang="de">
<head>
<meta charset="utf-8">
<title>Kugelwerk – Visitenkarte</title>
<link rel="stylesheet" href="https://fonts.googleapis.com/css2?family=Cookie&family=Federo&family=Open+Sans:wght@400&family=Oswald:wght@400&display=swap">
<style>
  :root{
    --brown:#38200f;
    --cream:#e9dcbc;
    --cream-soft:#ddcfae;
    --stone:#d8d2c2;
    --bead-dark:#2e3330;
    --page:#ffffff;
    --ink:#000000;
  }
  html,body{margin:0;padding:0;overflow:hidden;}
  body{width:1200px;height:1000px;background:var(--page);position:relative;}
  .card{position:absolute;width:539px;height:347px;overflow:hidden;box-shadow:5px 5px 4px rgba(0,0,0,.15);}
  .card--front{left:44px;top:92px;}
  .card--back{left:615px;top:92px;background:var(--brown);}
  .card svg{position:absolute;left:0;top:0;}
  .bead-photo{position:absolute;inset:0;
    background:linear-gradient(172deg,#6d5a4e 0%,#d9cdbd 12%,#8f6f63 22%,#e6ded2 30%,#b79a8a 45%,#cfc4b8 60%,#7d5a55 80%,#c9b5a8 100%);}
  .front-name{position:absolute;left:0;top:0;width:539px;height:347px;margin:0;
    font-family:"Cookie",cursive;font-weight:400;color:var(--cream);line-height:1;}
  .front-name .company{position:absolute;left:40px;top:112px;font-size:96px;}
  .front-name .owner{position:absolute;left:80px;top:188px;font-size:62px;}
  .back-content{position:absolute;left:0;top:48px;width:539px;text-align:center;color:var(--cream-soft);
    font-family:"Open Sans",sans-serif;font-size:17px;line-height:24px;}
  .back-title{margin:0;font-family:"Federo",sans-serif;font-size:30px;line-height:34px;color:var(--cream);
    font-variant:small-caps;letter-spacing:1px;font-weight:400;}
  .back-claim{margin:2px 0 0;font-size:18px;line-height:26px;}
  .back-contact{margin:26px 0 0;font-style:normal;}
  .back-mail{display:inline-block;margin-top:27px;font-size:19px;padding:0 8px 4px;border-bottom:2px solid var(--cream-soft);}
  .label{position:absolute;top:470px;margin:0;font-family:"Oswald",sans-serif;font-weight:400;font-size:56px;
    color:var(--ink);transform:scaleX(.82);transform-origin:left top;}
  .label--front{left:42px;}
  .label--back{left:620px;}
</style>
</head>
<body>
  <section class="card card--front" aria-label="Vorderseite">
    <div class="bead-photo" role="img" aria-label="Fotografie aufgereihter bunter Holzperlenketten"></div>
    <svg width="539" height="347" viewBox="0 0 539 347" aria-hidden="true">
      <path d="M8 62 Q300 70 430 115 Q525 160 534 270 L534 347 L8 347 Z" fill="var(--brown)"/>
      <path d="M0 250 L539 300 L539 325 L0 275 Z" fill="var(--bead-dark)"/>
    </svg>
    <h1 class="front-name">
      <span class="company">Kugelwerk</span>
      <span class="owner">Malte Oswitz</span>
    </h1>
  </section>

  <section class="card card--back" aria-label="Rückseite">
    <svg width="539" height="347" viewBox="0 0 539 347" aria-hidden="true">
      <path d="M0 0 H539 V30 Q500 40 440 58 Q380 20 230 12 Q80 10 0 48 Z" fill="var(--stone)"/>
    </svg>
    <div class="back-content">
      <h2 class="back-title">Holzschmuck</h2>
      <p class="back-claim">Herstellung von individuellem Holz- und<br>Modeschmuck</p>
      <address class="back-contact">
        Malte Oswitz<br>
        Tel: 015239460518<br>
        Lindgarbweg 9<br>
        83127 Holmbach
      </address>
      <span class="back-mail">malteoswitz@postfeld.de</span>
    </div>
  </section>

  <p class="label label--front">Front</p>
  <p class="label label--back">Back</p>
</body>
</html>
```